Business Card & Email Signature Design || Upmarket + Luxury

Riverlume Honey, a New Zealand Manuka Honey company needs a Business Card & Email Signature design.

Our logo's are attached in Gold & Black versions, feel free to be creative with how you use the logo and it's patterns in your design.

Style:
- Looking for an Elegant, Luxurious, Upmarket feel.
- Black/Matte Black Card, Gold Foil, UV Embossing

Information to Add:

- Logo
- Company Name: Riverlume Honey
- Name: Mattias Brovell
- Title: Creative Director
- Phone: +64 2919 58 617
- Email: mattias@riverlumehoney.example
- Website: www.riverlumehoney.example

- Socials: ***For email Signature Only***
- Facebook: https://www.facebook.com/riverlumehoney/
- Instagram: https://www.instagram.com/riverlumehoney/

Target Market(s)

Asia/Europe Luxury, Upmarket

Contact Information for Business Card

- Logo
- Name: Mattias Brovell
- Phone: +64 2919 58 617

Font styles to use
Other font styles liked:
• Champagne & Limousines (Attached)

Requirements
Must have
• Business Card & Email Signature Design.

Looking for a Sleek, Luxury, Upmarket Design.

```html
<!DOCTYPE html>
<html lang="en">
<head>
<meta charset="utf-8">
<title>Riverlume Honey — Business Card</title>
<link href="https://fonts.googleapis.com/css2?family=Montserrat:wght@300;400;500;600&display=swap" rel="stylesheet">
<style>
  :root {
    --backdrop: #a3a3a3;
    --card-light: #e4e4e2;
    --card-dark: #1b1b1b;
    --gold: #b8892f;
    --gold-soft: #c9a04a;
  }
  html, body {
    margin: 0;
    padding: 0;
    width: 1200px;
    height: 1199px;
    overflow: hidden;
    background: var(--backdrop);
    font-family: "Montserrat", sans-serif;
  }
  .canvas {
    position: relative;
    width: 1200px;
    height: 1199px;
  }
  .card {
    position: absolute;
    left: 195px;
    width: 800px;
    height: 436px;
  }
  .card-front { top: 115px; background: var(--card-light); }
  .card-back  { top: 649px; background: var(--card-dark); }

  .front-brand {
    position: absolute;
    left: 40px;
    width: 325px;
    top: 240px;
    text-align: center;
    color: var(--gold);
    font-weight: 400;
    font-size: 22px;
    letter-spacing: 4px;
    text-transform: uppercase;
  }
  .divider {
    position: absolute;
    left: 387px;
    top: 146px;
    width: 1.5px;
    height: 147px;
    background: var(--gold-soft);
  }
  .contact {
    position: absolute;
    left: 434px;
    top: 142px;
    color: var(--gold);
  }
  .contact-name {
    margin: 0;
    font-size: 29px;
    font-weight: 600;
    letter-spacing: 1.5px;
    text-transform: uppercase;
    line-height: 1.1;
  }
  .contact-title {
    margin: 2px 0 22px;
    font-size: 19px;
    font-weight: 300;
    color: var(--gold-soft);
    letter-spacing: 0.5px;
  }
  .contact-list {
    list-style: none;
    margin: 0;
    padding: 0;
    font-size: 17px;
    font-weight: 300;
  }
  .contact-list li {
    display: flex;
    align-items: center;
    gap: 8px;
    height: 27px;
  }
  .contact-list svg { width: 13px; height: 13px; flex: none; }

  .seal {
    position: absolute;
    left: 253px;
    top: 72px;
    width: 292px;
    height: 292px;
    border: 1.5px solid var(--gold-soft);
    border-radius: 50%;
    box-sizing: border-box;
    display: flex;
    align-items: center;
    justify-content: center;
  }
  .seal-name {
    color: var(--gold-soft);
    font-weight: 400;
    font-size: 22px;
    letter-spacing: 4px;
    text-transform: uppercase;
    text-align: center;
  }
</style>
</head>
<body>
<main class="canvas">
  <section class="card card-front">
    <div class="front-brand">Riverlume Honey</div>
    <div class="divider"></div>
    <div class="contact">
      <h1 class="contact-name">Mattias Brovell</h1>
      <p class="contact-title">Creative Director</p>
      <ul class="contact-list">
        <li>
          <svg viewBox="0 0 16 16" aria-hidden="true"><path d="M4 1.5 6.3 5 4.9 6.5c.9 2 2.5 3.6 4.6 4.6L11 9.7l3.5 2.3-1.2 2.5C7 14.2 1.8 9 1.5 2.7z" fill="none" stroke="currentColor" stroke-width="1.2"/></svg>
          <span>+64 2919 58 617</span>
        </li>
        <li>
          <svg viewBox="0 0 16 16" aria-hidden="true"><rect x="1.5" y="3.5" width="13" height="9" fill="none" stroke="currentColor" stroke-width="1.2"/><path d="M1.5 3.5 8 9l6.5-5.5" fill="none" stroke="currentColor" stroke-width="1.2"/></svg>
          <span>mattias@riverlumehoney.example</span>
        </li>
        <li>
          <svg viewBox="0 0 16 16" aria-hidden="true"><circle cx="8" cy="8" r="6.5" fill="none" stroke="currentColor" stroke-width="1.1"/><ellipse cx="8" cy="8" rx="2.8" ry="6.5" fill="none" stroke="currentColor" stroke-width="1"/><path d="M1.5 8h13M2.5 5h11M2.5 11h11" stroke="currentColor" stroke-width="1"/></svg>
          <span>www.riverlumehoney.example</span>
        </li>
      </ul>
    </div>
  </section>

  <section class="card card-back">
    <div class="seal">
      <div class="seal-name">Riverlume<br>Honey</div>
    </div>
  </section>
</main>
</body>
</html>
```